Marlowe Holdings LLC - Business Cards

Need the following information on the cards:

Name: Dean R Vossler
Title: Chief Executive Manager

Business address:
412 N Ridgeview Lane #118
Linden Grove, Il 60412

Phone: (630) 555-0148 - Business
KPV FFL license number: 5-21-xxx-xx-xx-04519
Email: dean.vossler@marloweholdingsffl.com

Target Market(s)

Firearm owners

Industry/Entity Type

Firearms industry,

Contact Information for Business Card

Contact number, name and title, web page address, email, business address and kpv license number,

Requirements
Must have
• Name, title, business address, phone numbers, KPV license numbers, web page address and email address.
Nice to have
• Cellphone number,

```html
<!DOCTYPE html>
<html lang="en">
<head>
<meta charset="utf-8">
<title>Marlowe Holdings LLC – Business Cards</title>
<link rel="stylesheet" href="https://fonts.googleapis.com/css2?family=Kanit:wght@300;400;600&family=Lexend:wght@300&display=swap">
<style>
  :root {
    --backdrop: #d3d4d6;
    --card-edge: #ffffff;
    --front-fill: #e6e8eb;
    --back-fill: #231f20;
    --ink: #231f20;
    --accent: #d7262b;
    --paper: #ffffff;
  }
  * { margin: 0; padding: 0; box-sizing: border-box; }
  html, body { width: 1200px; height: 1200px; overflow: hidden; }
  body { background: var(--backdrop); font-family: "Kanit", sans-serif; color: var(--ink); position: relative; }

  .card { position: absolute; left: 208px; width: 783px; height: 447px; background: var(--card-edge);
          box-shadow: 8px 8px 8px rgba(0,0,0,0.35); }
  .card--front { top: 103px; }
  .card--back { top: 649px; }
  .card__face { position: absolute; left: 16px; top: 16px; width: 752px; height: 416px; }
  .card--front .card__face { background: var(--front-fill); }
  .card--back .card__face { background: var(--back-fill); }

  .brand-mark { position: absolute; text-align: center; }
  .brand-mark svg { position: absolute; left: 0; top: 0; }
  .brand-mark__name { position: absolute; left: 0; width: 100%; font-weight: 600; letter-spacing: 1px; line-height: 1.05; }
  .card--front .brand-mark { left: 85px; top: 110px; width: 200px; height: 200px; }
  .card--front .brand-mark__name { top: 62px; font-size: 28px; color: var(--accent); }
  .card--back .brand-mark { left: 268px; top: 85px; width: 216px; height: 216px; }
  .card--back .brand-mark__name { top: 66px; font-size: 31px; color: var(--paper); }

  .name-tab { position: absolute; left: 356px; top: 0; width: 40px; height: 111px; background: var(--ink); }
  .name-tab svg { position: absolute; left: 8px; top: 64px; }
  .person-name { position: absolute; left: 414px; top: 50px; font-size: 37px; line-height: 1; white-space: nowrap; }
  .person-name b { font-weight: 600; }
  .person-name span { font-weight: 400; }
  .person-rule { position: absolute; left: 414px; top: 89px; width: 262px; height: 2px; background: var(--accent); }
  .person-title { position: absolute; left: 414px; top: 93px; font-size: 18px; font-weight: 300; letter-spacing: 0.6px; line-height: 1.2; }

  .contact { position: absolute; left: 356px; display: flex; align-items: center; }
  .contact__icon { width: 40px; height: 40px; flex: none; display: flex; align-items: center; justify-content: center; }
  .contact__icon--dark { background: var(--ink); }
  .contact__icon--red { background: var(--accent); }
  .contact__text { margin-left: 18px; font-family: "Lexend", sans-serif; font-size: 21px; font-weight: 300;
                   line-height: 26px; white-space: nowrap; }
  .contact__text--small { font-size: 15px; }
  .contact--address { top: 178px; }
  .contact--phone { top: 238px; }
  .contact--license { top: 297px; }
  .contact--email { top: 357px; }

  .web-address { position: absolute; left: 0; width: 100%; top: 372px; text-align: center;
                 color: var(--paper); font-family: "Lexend", sans-serif; font-size: 25px; font-weight: 300; letter-spacing: 1.5px; }
</style>
</head>
<body>

<section class="card card--front">
  <div class="card__face">
    <div class="brand-mark">
      <svg width="200" height="200" viewBox="0 0 200 200" aria-hidden="true">
        <circle cx="100" cy="100" r="92" fill="none" stroke="#231f20" stroke-width="3"/>
      </svg>
      <div class="brand-mark__name">MARLOWE<br>HOLDINGS<br>LLC</div>
    </div>

    <div class="name-tab">
      <svg width="24" height="34" viewBox="0 0 24 34" aria-hidden="true">
        <circle cx="12" cy="9" r="7" fill="none" stroke="#fff" stroke-width="2.2"/>
        <path d="M2 32 v-6 q0-7 10-7 q10 0 10 7 v6 z" fill="none" stroke="#fff" stroke-width="2.2"/>
      </svg>
    </div>
    <div class="person-name"><b>Dean R</b> <span>Vossler</span></div>
    <div class="person-rule"></div>
    <div class="person-title">CHIEF EXECUTIVE MANAGER</div>

    <div class="contact contact--address">
      <div class="contact__icon contact__icon--dark">
        <svg width="22" height="28" viewBox="0 0 22 28" aria-hidden="true">
          <path d="M11 27 C4 18 1 14 1 10 a10 10 0 0 1 20 0 c0 4-3 8-10 17z" fill="#fff"/>
          <circle cx="11" cy="10" r="4" fill="#231f20"/>
        </svg>
      </div>
      <div class="contact__text">412 N Ridgeview Lane #118<br>Linden Grove, Il 60412</div>
    </div>

    <div class="contact contact--phone">
      <div class="contact__icon contact__icon--red">
        <svg width="28" height="28" viewBox="0 0 28 28" aria-hidden="true">
          <circle cx="14" cy="14" r="12" fill="none" stroke="#fff" stroke-width="2"/>
          <path d="M9 8 l3 0 l1 4 l-2 1 q1 3 4 4 l1-2 l4 1 l0 3 q-1 2-3 2 q-9-2-10-10 q0-2 2-3z" fill="#fff"/>
        </svg>
      </div>
      <div class="contact__text">(630) 555-0148</div>
    </div>

    <div class="contact contact--license">
      <div class="contact__icon contact__icon--dark">
        <svg width="28" height="20" viewBox="0 0 28 20" aria-hidden="true">
          <rect x="1" y="1" width="26" height="18" rx="2" fill="none" stroke="#fff" stroke-width="2"/>
          <circle cx="8" cy="8" r="2.5" fill="#fff"/>
          <path d="M4 15 q4-6 8 0z" fill="#fff"/>
          <rect x="14" y="6" width="10" height="2" fill="#fff"/>
          <rect x="14" y="10" width="10" height="2" fill="#fff"/>
          <rect x="14" y="14" width="7" height="2" fill="#fff"/>
        </svg>
      </div>
      <div class="contact__text">5-21-xxx-xx-xx-04519</div>
    </div>

    <div class="contact contact--email">
      <div class="contact__icon contact__icon--red">
        <svg width="28" height="20" viewBox="0 0 28 20" aria-hidden="true">
          <rect x="1" y="1" width="26" height="18" fill="#fff"/>
          <path d="M1 1 L14 11 L27 1" fill="none" stroke="#d7262b" stroke-width="2"/>
        </svg>
      </div>
      <div class="contact__text contact__text--small">dean.vossler@marloweholdingsffl.com</div>
    </div>
  </div>
</section>

<section class="card card--back">
  <div class="card__face">
    <div class="brand-mark">
      <svg width="216" height="216" viewBox="0 0 216 216" aria-hidden="true">
        <circle cx="108" cy="108" r="100" fill="none" stroke="#fff" stroke-width="3"/>
      </svg>
      <div class="brand-mark__name">MARLOWE<br>HOLDINGS<br>LLC</div>
    </div>
    <div class="web-address">www.yourcompany.com</div>
  </div>
</section>

</body>
</html>
```